Business Card Design and Basic Text Logo

We are looking for a business card design for an e-business company. Our business is the parent company of a few website businesses. The final logo and business card design will communicate a conservative but modern and expansive business

The Logo text is: 87Merchant
We would also like a basic text logo design for 87Merchant. The logo could also fill up the reverse side of the business card.

The colours we would like to use are:
White
Navy
Black

This is the text that will be added to the card:

Dean Colley
Business Development Manager

Phone: +61 417 658 294
Email: dean.colley@87merchant.com.au

Industry/Entity Type

Business

Logo Text

87Merchant

Logo styles of interest
Pictorial/Combination Logo
Requirements
Must have
• Modern and attractive design
Nice to have
• communicate a conservative but modern and expansive business
Should not have
• Should be too dull and plan
• But also should be overly colourful

```html
<!DOCTYPE html>
<html lang="en">
<head>
<meta charset="utf-8">
<title>87Merchant – Dean Colley</title>
<link rel="stylesheet" href="https://fonts.googleapis.com/css2?family=Sorts+Mill+Goudy&display=swap">
<style>
  :root {
    --paper: #ffffff;
    --navy: #1f5fae;
    --ink: #111111;
    --wave-light: #ccd8ea;
    --wave-mid: #aab9dc;
    --wave-deep: #8498c9;
  }
  html, body {
    margin: 0;
    padding: 0;
    width: 1200px;
    height: 733px;
    overflow: hidden;
    background: var(--paper);
  }
  .card {
    position: relative;
    width: 1200px;
    height: 733px;
    background: var(--paper);
    overflow: hidden;
    font-family: "Sorts Mill Goudy", "Goudy Old Style", Georgia, serif;
  }
  .wave-field {
    position: absolute;
    inset: 0;
    width: 1200px;
    height: 733px;
  }
  .rule-horizontal {
    position: absolute;
    left: 0;
    top: 143px;
    width: 1200px;
    height: 5px;
    background: var(--navy);
  }
  .rule-vertical {
    position: absolute;
    left: 178px;
    top: 0;
    width: 5px;
    height: 733px;
    background: var(--navy);
  }
  .brand-name {
    position: absolute;
    left: 206px;
    top: 30px;
    margin: 0;
    font-size: 82px;
    line-height: 1;
    font-weight: 400;
    color: var(--navy);
  }
  .contact {
    position: absolute;
    left: 249px;
    top: 220px;
    margin: 0;
    font-size: 44px;
    line-height: 56px;
    color: var(--ink);
  }
  .contact p { margin: 0; }
  .contact .person-name { color: var(--navy); }
  .contact .details { margin-top: 56px; }
</style>
</head>
<body>
  <div class="card">
    <svg class="wave-field" viewBox="0 0 1200 733" role="img" aria-label="Flowing blue wave illustration with curling swirls, light to deep periwinkle">
      <defs>
        <linearGradient id="wave-gradient" x1="0" y1="0" x2="1" y2="0">
          <stop offset="0" stop-color="var(--wave-light)"/>
          <stop offset="0.45" stop-color="var(--wave-mid)"/>
          <stop offset="1" stop-color="var(--wave-deep)"/>
        </linearGradient>
      </defs>
      <path d="M790 0 H1200 V733 H395 C470 640 560 560 640 470 C720 380 700 260 730 170 C750 110 760 50 790 0 Z" fill="url(#wave-gradient)"/>
    </svg>

    <div class="rule-horizontal"></div>
    <div class="rule-vertical"></div>

    <h1 class="brand-name">87Merchant</h1>

    <div class="contact">
      <p class="person-name">Dean Colley</p>
      <p class="person-role">Business Development Manager</p>
      <div class="details">
        <p class="phone">Phone: +61 417 658 294</p>
        <p class="email">Email: dean.colley@87merchant.com.au</p>
      </div>
    </div>
  </div>
</body>
</html>
```